ebook cover for book three in a spiritual iconic series: bold, simple, easy to manage!

The Hollow is the third in a series of memoirs about one woman's spiritual journey over ten years. A PhD, the woman wants to appeal to a broad market and an intellectual market as well as the women's market that makes the core audience. Any Old Kettle is the second book and its cover is currently also commissioned here on Pixel Market if you want to search it. We Grow Radish was the first and its cover is attached for your reference. Please keep the same: the white background, the shade of red for the title, the font for the subtitle and colour, but change the title font and how you use the colour scheme. We look for a slightly enigmatic and also strikingly simple image. The tin can in We Grow Radish is where to start. For Any Old Kettle we have asked for a single Wordlark tablet, the X. Here, we are thinking of the winking smiley attached, but the image needs some photoshopping to make the face a bit more to yellow cold, remove the red ring and so on. The colours to pick from are greys, purple, red, orange, yellow, as with the colors in the flash of light on the tin can in Grow Radish. The idea there was to capture an explosion to new ideas while referencing a key scene involving cooking with tomatoes!

The Hollow

Book details:
Title: The Hollow
Subtitle: Brother Osric presents Veldora
Image ideas: Winking smiley attached, princess castle in the right colours, magic wand.
Author: Marla Quince, Ph.D
Strap quote: "Marla Quince is phenomenal in the true sense of the word. Phenomenons occur around her," Paula Drent, Teacher and spiritual healer

```html
<!DOCTYPE html>
<html lang="en">
<head>
<meta charset="utf-8">
<title>The Hollow — Marla Quince Ph.D.</title>
<link rel="stylesheet" href="https://fonts.googleapis.com/css2?family=Anton&family=Open+Sans:wght@300;400;600&display=swap">
<style>
  :root {
    --backdrop: #ecebec;
    --cover-white: #ffffff;
    --title-red: #b8121a;
    --title-red-deep: #a10f16;
    --ink: #1c1c1c;
    --author-grey: #5f5f5f;
    --sun-yellow: #fbf200;
    --sun-amber: #f1cf00;
    --shadow-soft: rgba(90, 90, 90, 0.28);
  }
  * { margin: 0; padding: 0; box-sizing: border-box; }
  html, body {
    width: 1200px;
    height: 800px;
    overflow: hidden;
    background: var(--backdrop);
  }
  .canvas {
    position: relative;
    width: 1200px;
    height: 800px;
    display: flex;
    align-items: center;
    justify-content: center;
  }
  .cover {
    position: relative;
    width: 514px;
    height: 760px;
    background: var(--cover-white);
    box-shadow: 0 6px 18px rgba(0, 0, 0, 0.12);
    font-family: "Open Sans", sans-serif;
    text-align: center;
  }
  .strap-quote {
    position: absolute;
    top: 24px;
    left: 40px;
    right: 40px;
    font-size: 9.5px;
    font-weight: 600;
    line-height: 1.2;
    color: var(--ink);
    text-transform: uppercase;
  }
  .strap-quote cite {
    display: block;
    margin-top: 3px;
    font-style: normal;
    font-size: 11.5px;
  }
  .book-title {
    position: absolute;
    top: 80px;
    left: 0;
    right: 0;
    font-family: "Anton", sans-serif;
    font-weight: 400;
    font-size: 84px;
    line-height: 1;
    letter-spacing: 0.01em;
    color: var(--title-red);
    background: linear-gradient(180deg, var(--title-red) 0%, var(--title-red-deep) 100%);
    -webkit-background-clip: text;
    background-clip: text;
    -webkit-text-fill-color: transparent;
  }
  .book-subtitle {
    position: absolute;
    top: 190px;
    left: 0;
    right: 0;
    font-size: 27px;
    font-weight: 400;
    line-height: 1.15;
    letter-spacing: 0.2em;
    color: var(--ink);
    text-transform: uppercase;
  }
  .cover-image {
    position: absolute;
    top: 335px;
    left: 111px;
    width: 292px;
    height: 345px;
  }
  .author {
    position: absolute;
    bottom: 36px;
    left: 0;
    right: 0;
    font-size: 31px;
    font-weight: 300;
    letter-spacing: 0.04em;
    color: var(--author-grey);
  }
  .author .degree { font-variant: small-caps; }
</style>
</head>
<body>
  <main class="canvas">
    <article class="cover">
      <blockquote class="strap-quote">
        “Marla Quince is phenomenal in the true sense of the word,<br>phenomenons occur around her,”
        <cite>- Paula Drent, Teacher and Spiritual Healer</cite>
      </blockquote>

      <h1 class="book-title">THE HOLLOW</h1>
      <h2 class="book-subtitle">Brother Osric<br>presents Veldora</h2>

      <svg class="cover-image" viewBox="0 0 292 345" role="img" aria-label="Illustration of a yellow winking smiley face floating above a soft shadow">
        <defs>
          <radialGradient id="sun-fill" cx="0.4" cy="0.35" r="0.7">
            <stop offset="0" stop-color="var(--sun-yellow)"/>
            <stop offset="0.75" stop-color="var(--sun-yellow)"/>
            <stop offset="1" stop-color="var(--sun-amber)"/>
          </radialGradient>
          <radialGradient id="ground-shadow" cx="0.5" cy="0.5" r="0.5">
            <stop offset="0" stop-color="var(--shadow-soft)"/>
            <stop offset="1" stop-color="rgba(90,90,90,0)"/>
          </radialGradient>
        </defs>
        <ellipse cx="146" cy="325" rx="150" ry="18" fill="url(#ground-shadow)"/>
        <circle cx="146" cy="146" r="146" fill="url(#sun-fill)"/>
      </svg>

      <p class="author">MARLA QUINCE <span class="degree">Ph.D.</span></p>
    </article>
  </main>
</body>
</html>
```